Slider images for online fax service homepage

QuillSend® needs 4 slider images for our newly designed homepage. The slider images should convey professionalism and simplicity without feeling cold or stuffy. The 4th slide is the only one that will contain a video and should be designed with that in mind. Attached to this contest, you will find two .pdf files. One contains a mockup of the new homepage containing dimensions and font requirements. The other is a spreadsheet containing copy for each slide.
In case you are unfamiliar with the brand, QuillSend® is the industry leader in online fax services. We provide faxing capabilities from mobile phones, tablets, and computers with state-of-the-art functionality, such as the ability to sign documents with your finger and send a document to any fax number directly from email.
Updates

FYI:  The dimensions of the video are 640x360.

Hello designers,

We don't want you to think we've forgotten about this contest.  We've been delayed in user testing but hope to have a response soon.

Thank you.

Target Market(s)

Mobile professionals and small businesses who need 24/7 access to fax services, such as lawyers, realtors, truckers, etc.

Industry/Entity Type

Industry

Requirements
Must have
• • The final deliverable should consist of a layered .psd file.
• Dimensions : 1500x475 (viewable area is 1200x475)
• Font is Google font – Lato
• Headline 62pt
• Subhead 32 pt

```html
<!DOCTYPE html>
<html lang="en">
<head>
<meta charset="utf-8">
<title>QuillSend® – The Fast, Smart &amp; Secure Way To Fax</title>
<link rel="stylesheet" href="https://fonts.googleapis.com/css2?family=Lato:wght@300;400;700;900&display=swap">
<style>
  :root {
    --bg-light: #f7f7f7;
    --bg-mid: #ececec;
    --bg-soft: #e4e4e4;
    --ink: #2b2b2b;
    --ink-soft: #333333;
    --accent: #e3161b;
    --button: #000000;
    --button-text: #ffffff;
    --photo-hair: #d9c29a;
    --photo-jacket: #d6d6d8;
    --photo-warm: #efe6e2;
  }
  * { margin: 0; padding: 0; box-sizing: border-box; }
  html, body {
    width: 1200px;
    height: 381px;
    overflow: hidden;
    background: var(--bg-light);
  }
  .hero-slide {
    position: relative;
    width: 1200px;
    height: 381px;
    overflow: hidden;
    font-family: "Lato", sans-serif;
    background:
      radial-gradient(ellipse 420px 260px at 260px 120px, #ffffff 0%, rgba(255,255,255,0) 100%),
      linear-gradient(100deg, var(--bg-mid) 0%, var(--bg-light) 35%, #fafafa 55%, var(--bg-soft) 78%, var(--bg-mid) 100%);
  }
  .hero-photo {
    position: absolute;
    left: 700px;
    top: 0;
    width: 500px;
    height: 381px;
    background:
      radial-gradient(ellipse 110px 190px at 255px 200px, var(--photo-hair) 0%, rgba(217,194,154,0.55) 55%, rgba(217,194,154,0) 100%),
      radial-gradient(ellipse 170px 150px at 265px 330px, var(--photo-jacket) 0%, rgba(214,214,216,0) 100%),
      linear-gradient(90deg, rgba(247,247,247,0) 0%, var(--photo-warm) 55%, rgba(236,236,236,0.6) 100%);
  }
  .hero-copy {
    position: absolute;
    left: 122px;
    top: 112px;
  }
  .hero-headline {
    font-weight: 300;
    font-size: 50px;
    line-height: 58px;
    letter-spacing: -1.8px;
    color: var(--ink);
    white-space: nowrap;
  }
  .hero-headline .highlight {
    color: var(--accent);
    font-weight: 400;
  }
  .hero-subhead {
    margin-top: 2px;
    font-weight: 400;
    font-size: 24px;
    line-height: 27px;
    color: var(--ink-soft);
    white-space: nowrap;
  }
  .hero-subhead .tagline {
    display: block;
    color: var(--accent);
  }
  .cta-button {
    display: inline-flex;
    align-items: center;
    justify-content: center;
    gap: 9px;
    margin-top: 16px;
    width: 262px;
    height: 47px;
    background: var(--button);
    color: var(--button-text);
    border-radius: 2px;
    font-weight: 900;
    font-size: 18px;
    letter-spacing: -0.2px;
    text-decoration: none;
  }
  .cta-button svg { width: 21px; height: 21px; }
</style>
</head>
<body>
  <section class="hero-slide">
    <div class="hero-photo" role="img" aria-label="Smiling woman with long blonde hair in a light grey blazer using a tablet at a white desk"></div>
    <div class="hero-copy">
      <h1 class="hero-headline">The <span class="highlight">Fast</span>, Smart &amp; Secure Way To Fax</h1>
      <p class="hero-subhead">Send and receive faxes easily and securely by email.
        <span class="tagline">No paper needed.</span></p>
      <a class="cta-button" href="#start">START FAXING
        <svg viewBox="0 0 22 22" aria-hidden="true">
          <circle cx="11" cy="11" r="9.5" fill="none" stroke="currentColor" stroke-width="1.6"/>
          <path d="M7 7 L11 11 L7 15 M11 7 L15 11 L11 15" fill="none" stroke="currentColor" stroke-width="1.8" stroke-linecap="round" stroke-linejoin="round"/>
        </svg>
      </a>
    </div>
  </section>
</body>
</html>
```